Brightoak Business Card

Professional Business Card Design required using the attached contact information.

Contact information can be rearranged as required.

The company is a new start up venture developing solar systems, the branding should be in keeping with that of one of the investors whose website is as follows https://www.corvellan.com/

```html
<!DOCTYPE html>
<html lang="en">
<head>
<meta charset="utf-8">
<title>Brightoak Renewables Business Card</title>
<link href="https://fonts.googleapis.com/css2?family=Roboto:wght@400&family=Saira:wght@400;600&display=swap" rel="stylesheet">
<style>
  :root {
    --backdrop: #3a3a3c;
    --card: #ffffff;
    --ink: #111111;
    --brand-green: #2f6e5a;
    --icon-green: #3f9a4a;
  }
  * { margin: 0; padding: 0; box-sizing: border-box; }
  html, body { width: 1200px; height: 881px; overflow: hidden; }
  body { background: var(--backdrop); position: relative; }

  .card {
    position: absolute;
    left: 355px;
    width: 487px;
    height: 278px;
    background: var(--card);
    color: var(--ink);
  }
  .card--front { top: 131px; }
  .card--back { top: 472px; }

  .wordmark {
    position: absolute;
    display: flex;
    align-items: center;
    font-family: "Saira", sans-serif;
    font-weight: 600;
    color: var(--ink);
    text-transform: uppercase;
    white-space: nowrap;
  }
  .wordmark__dot {
    display: inline-block;
    border-radius: 50%;
    background: var(--brand-green);
  }
  .card--front .wordmark {
    right: 24px;
    top: 46px;
    font-size: 13px;
    letter-spacing: 1.6px;
    gap: 7px;
  }
  .card--front .wordmark__dot { width: 8px; height: 8px; }
  .card--back .wordmark {
    left: 0; right: 0;
    top: 124px;
    justify-content: center;
    font-size: 25px;
    letter-spacing: 2.6px;
    gap: 12px;
  }
  .card--back .wordmark__dot { width: 14px; height: 14px; }

  .holder {
    position: absolute;
    left: 34px;
    top: 75px;
    font-family: "Roboto", sans-serif;
  }
  .holder__name { font-size: 19px; line-height: 22px; }
  .holder__role { font-size: 14px; line-height: 18px; }

  .contact {
    position: absolute;
    left: 32px;
    top: 172px;
    list-style: none;
    font-family: "Saira", sans-serif;
    font-weight: 400;
    font-size: 13px;
    line-height: 17px;
    letter-spacing: 0.4px;
  }
  .contact__item {
    display: flex;
    align-items: flex-start;
    gap: 9px;
    margin-bottom: 3px;
  }
  .contact__item:last-child { margin-top: 5px; }
  .contact__icon { width: 12px; height: 14px; flex: none; margin-top: 1px; fill: var(--icon-green); }
</style>
</head>
<body>

  <section class="card card--front">
    <div class="wordmark"><span class="wordmark__dot"></span>Brightoak Renewables</div>

    <div class="holder">
      <div class="holder__name">Daniel Whitcombe</div>
      <div class="holder__role">Owner</div>
    </div>

    <ul class="contact">
      <li class="contact__item">
        <svg class="contact__icon" viewBox="0 0 12 14" aria-hidden="true">
          <path d="M2.3 0.6l2 2.4c.3.4.3.9 0 1.2L3.5 5c.6 1.6 1.8 3.1 3.3 4l.9-.8c.4-.3.9-.3 1.2 0l2.3 2c.4.3.4.9.1 1.2l-1.1 1.3c-.5.6-1.4.8-2.1.4C4.6 11.6 1.6 7.9.6 4.3.4 3.5.6 2.7 1.2 2.2z"/>
        </svg>
        <span>+1 (555) 014-2738</span>
      </li>
      <li class="contact__item">
        <svg class="contact__icon" viewBox="0 0 12 14" aria-hidden="true">
          <path d="M0 4h12v1L6 8.6 0 5z M0 6.3l6 3.6 6-3.6V12H0z"/>
        </svg>
        <span>daniel.whitcombe@brightoak-renewables.com</span>
      </li>
      <li class="contact__item">
        <svg class="contact__icon" viewBox="0 0 12 16" style="height:16px" aria-hidden="true">
          <path d="M6 0a6 6 0 0 1 6 6c0 4-6 10-6 10S0 10 0 6a6 6 0 0 1 6-6zm0 3.2a2.8 2.8 0 1 0 0 5.6 2.8 2.8 0 0 0 0-5.6z"/>
        </svg>
        <span>Brightoak Renewables LLC<br>218 Harborline Street, Boston, MA 02110</span>
      </li>
    </ul>
  </section>

  <section class="card card--back">
    <div class="wordmark"><span class="wordmark__dot"></span>Brightoak Renewables</div>
  </section>

</body>
</html>
```